New Web Design Project

See attachments on the content and concept. Very important that the flow of the tiers stand out

Target Market(s)

Food and Beverage Manufacturing

Industry/Entity Type

Food and Beverage

Coding

Coded - Design and coding required

Number of Pages Required

3 page

Colors
0054AA
0677BA
7BADD7
CADEEF
E8F1F8

```html
<!DOCTYPE html>
<html lang="en">
<head>
<meta charset="utf-8">
<title>Northline Consulting Group — SQF Certification</title>
<link href="https://fonts.googleapis.com/css2?family=Playfair+Display:ital,wght@0,500;0,600;0,700;1,500&family=Montserrat:ital,wght@0,400;0,500;0,600;0,700;1,400&display=swap" rel="stylesheet">
<style>
:root{
  --blue:#0054AA;
  --blue-mid:#0677BA;
  --blue-soft:#7BADD7;
  --blue-pale:#CADEEF;
  --blue-mist:#E8F1F8;
  --ink:#1b1f2a;
  --muted:#6b7280;
  --white:#ffffff;
  --serif:'Playfair Display', Georgia, serif;
  --sans:'Montserrat', Arial, sans-serif;
}
*{box-sizing:border-box;margin:0;padding:0}
html,body{width:1200px;height:3909px;overflow:hidden}
body{position:relative;font-family:var(--sans);color:var(--ink);background:var(--white)}
.abs{position:absolute}
a{color:inherit;text-decoration:none}

/* nav */
.topbar{left:0;top:0;width:1200px;height:4px;background:var(--blue-soft)}
.nav{left:0;top:4px;width:1200px;height:76px;background:#f7f9fb;border-bottom:1px solid #e3e8ee}
.brand{left:144px;top:18px;display:flex;align-items:center;gap:12px}
.brand-mark{width:26px;height:26px;border:2px solid var(--ink);border-radius:50%}
.brand-name{font-family:var(--sans);font-weight:600;font-size:16px;color:var(--ink);line-height:1.2}
.brand-name small{display:block;font-size:10.5px;font-weight:500;letter-spacing:1.2px;color:var(--muted)}
.menu{left:461px;top:30px;display:flex;gap:36px;font-size:15px;color:var(--ink)}
.menu .active{color:var(--blue)}
.btn{display:inline-flex;align-items:center;justify-content:center;gap:10px;border-radius:30px;font-weight:600;font-size:16px}
.btn svg{width:18px;height:18px}
.btn-nav{left:831px;top:20px;width:225px;height:44px;background:var(--blue);color:#fff;font-size:15px}

/* hero */
.hero{left:0;top:80px;width:1200px;height:655px;background:linear-gradient(90deg,#0a4f9e 0%,#0e5aa8 45%,#3f6fa8 70%,#8fa9c8 100%);overflow:hidden}
.hero-photo{left:560px;top:0;width:640px;height:655px;background:linear-gradient(100deg,rgba(14,90,168,0) 0%,rgba(190,205,222,.55) 50%,rgba(225,232,240,.8) 100%)}
.hero-wave{left:0;top:0;width:1200px;height:655px}
.eyebrow{font-size:14px;letter-spacing:.5px;color:#dfe9f5;text-transform:uppercase}
.hero .eyebrow{left:144px;top:66px}
.hero-title{left:144px;top:96px;width:640px;font-family:var(--serif);font-weight:700;font-size:47px;line-height:56px;color:#fff}
.hero-rule{left:0;top:343px;width:397px;height:3px;background:#fff}
.hero-dots{left:402px;top:343px;width:14px;height:3px;background:repeating-linear-gradient(90deg,#fff 0 4px,transparent 4px 7px)}
.hero-copy{left:144px;top:370px;width:520px;font-size:19px;line-height:29px;color:#fff}
.btn-light{left:144px;top:524px;width:263px;height:50px;background:var(--blue-pale);color:var(--blue)}
.btn-ghost{left:416px;top:524px;width:223px;height:50px;border:2px solid #fff;color:#fff}

/* section heads */
.sec-label{width:1200px;left:0;text-align:center;font-size:14px;letter-spacing:.6px;color:var(--blue);text-transform:uppercase}
.sec-title{width:1200px;left:0;text-align:center;font-family:var(--serif);font-weight:600;font-size:38px;color:var(--ink)}
.sec-rule{left:566px;width:68px;height:2px;background:var(--blue-soft)}
.sec-sub{left:230px;width:740px;text-align:center;font-size:14px;line-height:24px;color:var(--muted)}

/* steps */
.step{width:437px;height:267px;background:#fff;box-shadow:0 4px 22px rgba(20,50,90,.09)}
.step-icon{position:absolute;left:29px;top:27px;width:80px;height:80px;background:var(--blue-mist);border-radius:4px;display:flex;align-items:center;justify-content:center}
.step-icon svg{width:46px;height:46px;fill:none;stroke:var(--blue);stroke-width:1.8;stroke-linecap:round;stroke-linejoin:round}
.step-num{position:absolute;right:28px;top:42px;font-family:var(--serif);font-weight:600;font-size:38px;color:var(--blue)}
.step-title{position:absolute;left:32px;top:133px;font-size:17px;font-weight:500}
.step-text{position:absolute;left:32px;top:170px;width:385px;font-size:14px;line-height:24px;color:var(--muted)}

/* stats */
.stats{left:0;top:1612px;width:1200px;height:201px;background:var(--blue)}
.stat-icon{width:80px;height:80px;fill:none;stroke:#fff;stroke-width:2.2;stroke-linecap:round;stroke-linejoin:round}
.stat-num{font-family:var(--serif);font-weight:600;color:#fff;line-height:1}
.stat-cap{font-size:14px;color:#fff}

/* why */
.why-photo{left:112px;top:2083px;width:976px;height:443px;background:linear-gradient(180deg,#d9dee4 0%,#b9c1ca 55%,#8d949c 100%)}
.benefit{background:#fff;border:1px solid #e1e6ec;text-align:center;padding:24px 22px}
.benefit h3{font-weight:500;font-size:15.5px;color:var(--ink);margin-bottom:12px}
.benefit p{font-size:13.5px;line-height:22px;color:var(--muted)}

/* testimonial */
.quote-band{left:0;top:2849px;width:1200px;height:370px;background:var(--blue-mist)}
.quote-mark{left:548px;top:2905px;width:104px;height:76px}
.quote-text{left:150px;top:2996px;width:900px;text-align:center;font-style:italic;font-size:23px;line-height:40px;color:#2d3340}
.quote-cite{left:0;top:3140px;width:1200px;text-align:center;font-family:var(--serif);font-weight:500;font-size:17px;color:var(--blue)}

/* cta */
.cta-title{left:0;top:3292px;width:1200px;text-align:center;font-family:var(--serif);font-weight:700;font-size:52px;color:var(--ink)}
.cta-sub{left:240px;top:3383px;width:720px;text-align:center;font-size:14px;line-height:24px;color:var(--muted)}
.btn-primary{left:272px;top:3475px;width:264px;height:52px;background:var(--blue);color:#fff}
.btn-soft{left:552px;top:3475px;width:376px;height:52px;background:var(--blue-mist);color:var(--blue)}

/* footer */
.footer{left:0;top:3598px;width:1200px;height:311px}
.foot-col h4{font-size:15px;font-weight:500;color:#fff;letter-spacing:.5px;text-transform:uppercase;margin-bottom:17px}
.foot-col li{list-style:none;font-size:14.5px;color:#fff;line-height:24px}
.contact-row{display:flex;align-items:flex-start;gap:12px;font-size:14.5px;color:#fff;line-height:24px;margin-bottom:15px}
.contact-dot{flex:none;width:24px;height:24px;border-radius:50%;background:#fff;display:flex;align-items:center;justify-content:center}
.contact-dot svg{width:13px;height:13px;fill:var(--blue)}
.foot-line{left:144px;top:3864px;width:912px;height:1px;background:rgba(255,255,255,.25)}
.copyright{left:0;top:3878px;width:1200px;text-align:center;font-size:14px;color:#fff}
</style>
</head>
<body>

<div class="abs topbar"></div>
<header class="abs nav">
  <div class="abs brand"><span class="brand-mark"></span><span class="brand-name">Northline Consulting Group<small>FOOD SAFETY &amp; SQF CERTIFICATION</small></span></div>
  <nav class="abs menu"><a class="active">Services</a><a>Benefits</a><a>Process</a><a>Contact</a></nav>
  <a class="abs btn btn-nav">Get SQF Consultation</a>
</header>

<section class="abs hero">
  <div class="abs hero-photo" role="img" aria-label="Food safety professional holding a tablet with a compliance checklist in a production facility"></div>
  <svg class="abs hero-wave" viewBox="0 0 1200 655" preserveAspectRatio="none"><path d="M0 655 L0 640 C400 640 800 630 1200 600 L1200 655 Z" fill="#7BADD7"/><path d="M0 655 L0 648 C420 650 760 645 1200 630 L1200 655 Z" fill="#fff"/></svg>
  <p class="abs eyebrow">SQF Only Tech Driven</p>
  <h1 class="abs hero-title">Hire a Tech Driven SQF Team That Carries You Across The Certification Finish Line.</h1>
  <div class="abs hero-rule"></div><div class="abs hero-dots"></div>
  <p class="abs hero-copy">At Northline Consulting Group, we focus exclusively on SQF combining real plant experience with smart technology so your team can stay focused on production while we handle the path to certification and beyond.</p>
  <a class="abs btn btn-light">Get SQF Consultation <svg viewBox="0 0 24 24" fill="none" stroke="currentColor" stroke-width="2"><path d="M4 12h15M13 6l6 6-6 6"/></svg></a>
  <a class="abs btn btn-ghost">Explore Services <svg viewBox="0 0 24 24" fill="none" stroke="currentColor" stroke-width="2"><path d="M4 12h15M13 6l6 6-6 6"/></svg></a>
</section>

<p class="abs sec-label" style="top:797px">How It Works</p>
<h2 class="abs sec-title" style="top:820px">From Discovery To Certification</h2>
<div class="abs sec-rule" style="top:894px"></div>
<p class="abs sec-sub" style="top:908px">A clear, structured path that takes the guesswork out of SQF</p>

<article class="abs step" style="left:144px;top:969px">
  <div class="step-icon"><svg viewBox="0 0 48 48"><circle cx="24" cy="18" r="8"/><path d="M14 18a10 10 0 0 1 20 0M12 42c0-7 5-12 12-12s12 5 12 12z"/><rect x="12" y="16" width="3" height="6"/><rect x="33" y="16" width="3" height="6"/></svg></div>
  <span class="step-num">01</span><h3 class="step-title">Discovery Call</h3>
  <p class="step-text">We learn about your facility, your current systems, and where you are in the SQF journey. No pressure-just a conversation.</p>
</article>
<article class="abs step" style="left:617px;top:969px">
  <div class="step-icon"><svg viewBox="0 0 48 48"><rect x="10" y="8" width="24" height="32" rx="2"/><path d="M17 6h10v5H17zM15 18h3M21 18h8M15 24h3M21 24h8M15 30h3M21 30h5"/><circle cx="33" cy="32" r="6"/><path d="M37 36l5 5"/></svg></div>
  <span class="step-num">02</span><h3 class="step-title">Gap Assessment</h3>
  <p class="step-text">We evaluate your facility against SQF requirements, identify what's missing, and give you a clear roadmap with priorities.</p>
</article>
<article class="abs step" style="left:144px;top:1265px">
  <div class="step-icon"><svg viewBox="0 0 48 48"><circle cx="24" cy="24" r="7"/><path d="M24 8v5M24 35v5M8 24h5M35 24h5M12.7 12.7l3.5 3.5M31.8 31.8l3.5 3.5M12.7 35.3l3.5-3.5M31.8 16.2l3.5-3.5"/><circle cx="24" cy="24" r="13"/></svg></div>
  <span class="step-num">03</span><h3 class="step-title">Build &amp; Implement</h3>
  <p class="step-text">We design your SQF program and build it directly into your digital food safety platform-form legs, SOPs HACCP plans, all of it.</p>
</article>
<article class="abs step" style="left:617px;top:1265px">
  <div class="step-icon"><svg viewBox="0 0 48 48"><path d="M30 40H10V8h18l6 6v8"/><path d="M15 18h12M15 24h10M15 30h8"/><circle cx="34" cy="32" r="6"/><path d="M31 32l2 2 4-4M30 37l-2 6 6-3 6 3-2-6"/></svg></div>
  <span class="step-num">04</span><h3 class="step-title">Coach &amp; Certify</h3>
  <p class="step-text">We train your team, run mock audits and prepare you for certification day Then we stay on as your ongoing SQF advisory partner.</p>
</article>

<section class="abs stats">
  <svg class="abs stat-icon" style="left:144px;top:60px" viewBox="0 0 80 80"><circle cx="20" cy="14" r="6"/><circle cx="40" cy="12" r="6"/><circle cx="60" cy="14" r="6"/><path d="M8 36c0-8 5-12 12-12s12 4 12 12M28 32c1-7 6-10 12-10s11 3 12 10M48 36c0-8 5-12 12-12s12 4 12 12M10 48l16 22M70 48L54 70M24 56l12-8 10 4 10 10-6 6-12-10"/></svg>
  <div class="abs stat-num" style="left:250px;top:67px;font-size:46px">15+</div>
  <div class="abs stat-cap" style="left:252px;top:127px">Clients Onboarded</div>

  <svg class="abs stat-icon" style="left:479px;top:60px" viewBox="0 0 80 80"><circle cx="38" cy="40" r="10"/><path d="M38 14v8M38 58v8M12 40h8M56 40h8M20 22l6 6M50 52l6 6M20 58l6-6M50 28l6-6"/><circle cx="38" cy="40" r="20"/><circle cx="70" cy="24" r="3"/><circle cx="72" cy="40" r="3"/><circle cx="70" cy="56" r="3"/></svg>
  <div class="abs stat-num" style="left:577px;top:55px;font-size:54px">Digital</div>
  <div class="abs stat-cap" style="left:578px;top:127px">Platform Built Programs</div>

  <svg class="abs stat-icon" style="left:839px;top:60px" viewBox="0 0 80 80"><circle cx="36" cy="44" r="28"/><circle cx="36" cy="44" r="18"/><circle cx="36" cy="44" r="8"/><path d="M36 44L66 14M58 12l8 2 2 8"/></svg>
  <div class="abs stat-num" style="left:942px;top:55px;font-size:54px">100%</div>
  <div class="abs stat-cap" style="left:944px;top:127px">SQF Focused</div>
</section>

<p class="abs sec-label" style="top:1890px">Why Northline Consulting</p>
<h2 class="abs sec-title" style="top:1916px">Built for Small and Mid Size Manufacturers</h2>
<div class="abs sec-rule" style="top:1986px"></div>
<p class="abs sec-sub" style="top:2003px">You don't need to hire a full-time food safety director or figure out SQF alone. We bring the expertise and technology you stay focused on production.</p>
<div class="abs why-photo" role="img" aria-label="Food production line with staff in hairnets and lab coats inspecting products"></div>

<div class="abs benefit" style="left:144px;top:2450px;width:296px;height:165px"><h3>Lower Cost Than a Full-Time Hire</h3><p>Get a complete SQF team program design, digital implementation, and coaching at a fraction of the cost of hiring a full-time SQF Practitioner.</p></div>
<div class="abs benefit" style="left:451px;top:2450px;width:297px;height:165px"><h3>Your Program Lives in Software</h3><p>No more binders &amp; spreadsheets. Your SQF system is built into Checkpoint.ai or SafeLedger.ai audit ready. organized, accessible, and always.</p></div>
<div class="abs benefit" style="left:759px;top:2450px;width:295px;height:165px"><h3>Lower Cost Than a Full-Time Hire</h3><p>We build the system and train your team. You maintain and run it day to day. We stay on call with coaching and advisory so you never feel stuck.</p></div>
<div class="abs benefit" style="left:144px;top:2627px;width:448px;height:141px"><h3>Flexible, Low-Risk Engagement</h3><p>Start with a 3-month commitment, then go month-to-month. Cancel anytime with 30 days notice. We earn your business every month.</p></div>
<div class="abs benefit" style="left:605px;top:2627px;width:449px;height:141px"><h3>Flexible, Low-Risk Engagement</h3><p>Start with a 3-month commitment, then go month-to-month. Cancel anytime with 30 days notice. We earn your business every month.</p></div>

<section class="abs quote-band"></section>
<svg class="abs quote-mark" viewBox="0 0 104 76" fill="none" stroke="#0054AA" stroke-width="4" stroke-linejoin="round"><path d="M2 2h44v38c0 18-10 30-26 34l-4-8c8-4 12-10 12-20H2z"/><path d="M58 2h44v38c0 18-10 30-26 34l-4-8c8-4 12-10 12-20H58z"/></svg>
<p class="abs quote-text">Northline Consulting Group didn't just hand us a binder. They built our entire SQF system into software and coached our team until we owned it. We passed our first audit with confidence.</p>
<p class="abs quote-cite">SQF-Certified Manufacturing Client</p>

<h2 class="abs cta-title">Ready to Talk SQF?</h2>
<p class="abs cta-sub">Share a few details about your facility and where you are in the SQF journey. We'll follow up with a brief discovery call and a clear next step.</p>
<a class="abs btn btn-primary">Get SQF Consultation <svg viewBox="0 0 24 24" fill="none" stroke="currentColor" stroke-width="2"><path d="M4 12h15M13 6l6 6-6 6"/></svg></a>
<a class="abs btn btn-soft">Visit PlantSignal.ai <svg viewBox="0 0 24 24" fill="none" stroke="currentColor" stroke-width="2"><path d="M4 12h15M13 6l6 6-6 6"/></svg></a>

<footer class="abs footer">
  <svg class="abs" style="left:0;top:0" width="1200" height="311" viewBox="0 0 1200 311" preserveAspectRatio="none"><path d="M0 20 C400 40 800 30 1200 0 L1200 311 L0 311Z" fill="#7BADD7"/><path d="M0 38 C420 45 800 42 1200 22 L1200 311 L0 311Z" fill="#0054AA"/></svg>
</footer>
<div class="abs foot-col" style="left:144px;top:3677px"><h4>Quick Links</h4><ul><li>Home</li><li>Services</li><li>Benefits</li><li>Process</li><li>Contact</li></ul></div>
<div class="abs foot-col" style="left:318px;top:3677px"><h4>Services</h4><ul><li>SQF Program Design</li><li>Digital Platform Build</li><li>Coaching &amp; Support</li><li>Gap Assessments</li><li>Sanitation Programs</li></ul></div>
<div class="abs foot-col" style="left:553px;top:3677px"><h4>Connect</h4><ul><li>Email Us</li><li>PlantSignal.ai</li><li>Social Profile</li></ul></div>
<div class="abs foot-col" style="left:817px;top:3677px"><h4>Contact Us</h4>
  <div class="contact-row"><span class="contact-dot"><svg viewBox="0 0 24 24"><path d="M6.6 10.8a15 15 0 0 0 6.6 6.6l2.2-2.2c.3-.3.7-.4 1-.2 1.1.4 2.3.6 3.6.6.6 0 1 .4 1 1V20c0 .6-.4 1-1 1A17 17 0 0 1 3 4c0-.6.4-1 1-1h3.5c.6 0 1 .4 1 1 0 1.3.2 2.5.6 3.6.1.3 0 .7-.2 1z"/></svg></span>+1-555-014-2210</div>
  <div class="contact-row"><span class="contact-dot"><svg viewBox="0 0 24 24"><path d="M3 6h18v12H3zM3 6l9 7 9-7" fill="none" stroke="#0054AA" stroke-width="2.4"/></svg></span>hello@northlinegroup.com</div>
  <div class="contact-row"><span class="contact-dot"><svg viewBox="0 0 24 24"><path d="M12 2a7 7 0 0 0-7 7c0 5 7 13 7 13s7-8 7-13a7 7 0 0 0-7-7zm0 9.5A2.5 2.5 0 1 1 12 6.5a2.5 2.5 0 0 1 0 5z"/></svg></span>480 Harbor Lane, Suite 12<br>Riverton</div>
</div>
<div class="abs foot-line"></div>
<p class="abs copyright">2026 Copyright - Northline Consulting Group LLC</p>

</body>
</html>
```